The Velvet Lintel with an elephant incorporated in the background

Target Market(s)

Real estate

Industry/Entity Type

Real Estate

Contact Information for Business Card

On back on want my name & number
In front I want the business name, "the velvet lintel", below to say staging & design

Logo Text

The Velvet Lintel

Font styles to use
Serif

Colors
000000

Requirements
Must have
• I want an elephant behind the writing in gold transperant

```html
<!DOCTYPE html>
<html lang="en">
<head>
<meta charset="utf-8">
<title>The Velvet Lintel – Business Cards</title>
<link rel="stylesheet" href="https://fonts.googleapis.com/css2?family=Cinzel:wght@500;700&family=Cormorant+Garamond:wght@400;500&display=swap">
<style>
  :root {
    --backdrop: #2b2b2b;
    --card-dark-top: #4a4a4a;
    --card-dark-bottom: #2e2e2e;
    --card-light-top: #ffffff;
    --card-light-bottom: #e6e6e6;
    --ink-dark: #4b4b4b;
    --ink-light: #e9e9e9;
    --ink-muted: #c8c8c8;
    --rule: #bdbdbd;
    --gold-light: #f1d36a;
    --gold-mid: #c99a22;
    --gold-deep: #8a6410;
  }
  * { box-sizing: border-box; margin: 0; padding: 0; }
  html, body {
    width: 1200px;
    height: 997px;
    overflow: hidden;
    background: var(--backdrop);
  }
  .stage {
    position: relative;
    width: 1200px;
    height: 997px;
  }
  .card {
    position: absolute;
    top: 338px;
    width: 520px;
    height: 320px;
    border-radius: 26px;
    box-shadow: 0 18px 40px rgba(0,0,0,0.45);
    overflow: hidden;
  }

  /* Back of card */
  .card--back {
    left: 50px;
    background: linear-gradient(160deg, var(--card-dark-top), var(--card-dark-bottom));
  }
  .card--back .person {
    position: absolute;
    left: 56px;
    top: 70px;
    text-align: center;
  }
  .person__name {
    font-family: "Cinzel", serif;
    font-weight: 700;
    font-size: 26px;
    color: var(--ink-light);
    letter-spacing: 1px;
  }
  .person__role {
    margin-top: 10px;
    font-family: "Cormorant Garamond", serif;
    font-size: 17px;
    letter-spacing: 7px;
    color: var(--ink-muted);
  }
  .card--back .divider {
    position: absolute;
    left: 36px;
    right: 36px;
    top: 176px;
    height: 2px;
    background: var(--rule);
  }
  .contact {
    position: absolute;
    left: 150px;
    top: 212px;
    display: flex;
    align-items: center;
    gap: 14px;
    font-family: "Cormorant Garamond", serif;
    font-size: 21px;
    color: var(--ink-light);
    letter-spacing: 1px;
  }
  .contact__icon { width: 30px; height: 30px; }

  /* Front of card */
  .card--front {
    left: 630px;
    background: linear-gradient(160deg, var(--card-light-top), var(--card-light-bottom));
  }
  .brand {
    position: absolute;
    left: 0;
    right: 0;
    top: 46px;
    text-align: center;
  }
  .brand__name {
    font-family: "Cinzel", serif;
    font-weight: 500;
    font-size: 30px;
    color: var(--ink-dark);
    letter-spacing: 0.5px;
  }
  .brand__tagline {
    margin-top: 4px;
    font-family: "Cormorant Garamond", serif;
    font-size: 17px;
    letter-spacing: 11px;
    color: var(--ink-dark);
  }
  .emblem-art {
    position: absolute;
    left: 145px;
    top: 130px;
    width: 260px;
    height: 160px;
    border-radius: 40px;
    background: radial-gradient(ellipse at 45% 45%, var(--gold-light), var(--gold-mid) 55%, var(--gold-deep) 100%);
    opacity: 0.9;
  }
</style>
</head>
<body>
<main class="stage">
  <section class="card card--back" aria-label="Business card back">
    <div class="person">
      <p class="person__name">MILES HARROW</p>
      <p class="person__role">Property Consultant</p>
    </div>
    <div class="divider"></div>
    <div class="contact">
      <svg class="contact__icon" viewBox="0 0 30 30" aria-hidden="true">
        <circle cx="15" cy="15" r="14" fill="#d9d9d9"/>
        <rect x="10.5" y="7" width="9" height="16" rx="1.6" fill="none" stroke="#3a3a3a" stroke-width="1.6"/>
        <line x1="13.5" y1="20.5" x2="16.5" y2="20.5" stroke="#3a3a3a" stroke-width="1.4"/>
      </svg>
      <span class="contact__phone">07418 362950</span>
    </div>
  </section>

  <section class="card card--front" aria-label="Business card front">
    <div class="brand">
      <p class="brand__name">THE VELVET LINTEL</p>
      <p class="brand__tagline">STAGING &amp; DESIGN</p>
    </div>
    <div class="emblem-art" role="img" aria-label="Gold elephant figure with raised trunk"></div>
  </section>
</main>
</body>
</html>
```